Web Design for ORV Air conditioning company

Hello,

I am calling on you for the modernization of the company's website
https://clim-solaris-atelier.fr/

The new one must include the new logo with the new graphic charter (color, style ...)

I'm looking for a simple design (less is more), a font written without Serif, the logo that brings a touch of color and modernity.

(maintenance and installation company for air conditioning and ventilation systems)
COLORS: in line with the logo

CHAPTER:

# PRESENTATION
# SERVICES
AIR CONDITIONING (ice cube icon)
HEATING (flame icon)
AIR TREATMENT (icon fan)
# ACHIEVEMENTS

# CONTACT
CONTACT FORM
GOOGLE MAPS

Target Market(s)

Showcase site for our customers

Coding

Coded - Design and coding required

Number of Pages Required

4 page

Font styles to use
Sans Serif

Colors
33b8a4
33a6d7
3176b5
ffffff

Requirements
Must have
• Clear and fluid navigation
a visual identity of the page with the logo
Should not have
• Overloaded.

```html
<!DOCTYPE html>
<html lang="en">
<head>
<meta charset="utf-8">
<title>ORV – Climate Solutions Atelier</title>
<link href="https://fonts.googleapis.com/css2?family=Raleway:wght@500;600;700&family=Open+Sans:wght@400;600&display=swap" rel="stylesheet">
<style>
:root{
  --teal:#33b8a4;
  --sky:#33a6d7;
  --blue:#3176b5;
  --white:#ffffff;
  --ink:#222222;
  --text:#555555;
  --dark:#2b2b2b;
}
*{box-sizing:border-box;margin:0;padding:0}
html,body{width:1200px;height:3699px;overflow:hidden}
body{position:relative;background:var(--white);font-family:"Open Sans",Arial,sans-serif;color:var(--text)}
.abs{position:absolute}
h1,h2,h3,.nav a,.btn,.brand{font-family:"Raleway",Arial,sans-serif}

/* header */
.brand{position:absolute;left:89px;top:20px;font-size:58px;font-weight:700;color:var(--blue);letter-spacing:2px;line-height:60px}
.nav{position:absolute;right:93px;top:47px;display:flex;gap:23px}
.nav a{font-size:15px;font-weight:600;color:var(--ink);text-decoration:none;padding-bottom:8px}
.nav a.active{border-bottom:3px solid var(--teal)}
.topbar{position:absolute;top:100px;left:0;width:1200px;height:50px;background:var(--teal);color:var(--white);font-family:"Raleway",sans-serif;font-weight:600;font-size:16.5px;text-align:center;line-height:50px}

/* hero */
.hero-photo{position:absolute;top:150px;left:0;width:1200px;height:595px;background:linear-gradient(120deg,#6d6f78 0%,#4b5a78 45%,#3c3f4c 75%,#5a5c64 100%)}
.hero-photo::after{content:"";position:absolute;inset:0;background:rgba(20,24,40,.35)}
.hero-title{position:absolute;top:330px;width:1200px;text-align:center;color:var(--white);font-size:49px;font-weight:600}
.hero-sub{position:absolute;top:405px;width:1200px;text-align:center;color:var(--white);font-size:17.5px;font-weight:600;line-height:27px}
.btn{display:block;text-align:center;text-decoration:none;font-weight:600}
.btn-fill{position:absolute;left:501px;top:478px;width:198px;height:57px;line-height:57px;background:var(--teal);color:var(--white);border-radius:4px;font-size:20px}

/* sections */
.section-title{position:absolute;width:1200px;text-align:center;color:var(--blue);font-size:41px;font-weight:600}
.lead{position:absolute;text-align:center;font-size:18.5px;line-height:36px}

.card{position:absolute;top:996px;width:416px;height:186px;color:var(--white)}
.card-left{left:89px;background:linear-gradient(135deg,var(--teal),var(--sky))}
.card-right{left:693px;background:linear-gradient(135deg,var(--sky),var(--teal))}
.card h3{position:absolute;top:24px;font-size:27px;font-weight:600}
.card p{position:absolute;top:65px;width:315px;font-size:14.3px;line-height:24px;hyphens:auto}
.card-left h3{right:100px}
.card-left p{left:16px;text-align:right}
.card-right h3{left:81px}
.card-right p{left:81px;text-align:justify}
.diamond{position:absolute;top:1023px;width:130px;height:130px}

.who-photo{position:absolute;top:1270px;left:0;width:527px;height:442px;background:linear-gradient(135deg,#8a8f96,#3b4a5e 55%,#c9a35b)}
.who-panel{position:absolute;top:1270px;left:527px;width:673px;height:442px;background:var(--teal);color:var(--white)}
.who-panel h2{position:absolute;left:64px;top:58px;font-size:41px;font-weight:600}
.who-panel p{position:absolute;left:64px;top:125px;width:522px;font-size:15px;line-height:31.4px;text-align:justify;hyphens:auto;letter-spacing:-0.1px}
.btn-line{position:absolute;left:64px;top:309px;width:198px;height:57px;line-height:53px;border:2px solid var(--white);border-radius:5px;color:var(--white);font-size:20px}

.service{position:absolute;top:1963px;width:310px;text-align:center}
.service .circle{width:310px;height:310px;border-radius:50%;overflow:hidden;position:relative}
.service h3{margin-top:30px;font-size:23px;font-weight:600;color:var(--ink)}
.circle-overlay{position:absolute;inset:0;border:4px solid var(--teal);border-radius:50%;background:rgba(40,45,55,.7);display:flex;align-items:center;justify-content:center;padding:0 38px;color:var(--white);font-size:16px;line-height:30px}

/* contact */
.contact{position:absolute;top:2412px;left:0;width:1200px;height:477px;background:var(--teal)}
.contact h2{position:absolute;top:28px;width:1200px;text-align:center;color:var(--white);font-size:41px;font-weight:600}
.field{position:absolute;background:var(--white);color:#666;font-size:17px;padding:0 9px;line-height:52px;border:0}
.field-area{line-height:28px;padding:14px 8px}
.btn-submit{position:absolute;left:501px;top:391px;width:198px;height:57px;line-height:53px;border:2px solid var(--white);border-radius:5px;color:var(--white);font-size:23px}

.map{position:absolute;top:2889px;left:0;width:1200px;height:400px;background:linear-gradient(160deg,#eef0f2,#e3e6e9 60%,#eceef0)}

/* footer */
.footer-text{position:absolute;color:var(--white)}
.footer-brand{position:absolute;left:89px;top:3332px;font-family:"Raleway",sans-serif;font-size:92px;font-weight:700;color:var(--white);letter-spacing:4px;line-height:92px}
.footer-about{left:89px;top:3458px;width:260px;font-size:15px;line-height:26.5px;text-align:justify}
.footer-col h3{font-size:21px;font-weight:600;margin-bottom:17px}
.footer-col li{list-style:none;font-size:16px;line-height:32.3px}
.copyright{top:3648px;width:1200px;text-align:center;font-family:"Raleway",sans-serif;font-size:19px}
</style>
</head>
<body>

<header>
  <div class="brand">ORV</div>
  <nav class="nav">
    <a class="active" href="#">HOME</a>
    <a href="#">WHO ARE WE</a>
    <a href="#">OUR SERVICES</a>
    <a href="#">PRESENTATION</a>
    <a href="#">ACHIEVEMENTS</a>
    <a href="#">CONTACT</a>
  </nav>
</header>

<div class="topbar">LOREM IPSUM DOLOR SIT AMET, CONSECTETUR ADIPISCING ELIT, SED DO EIUSMOD TEMPOR INCIDIDUNT</div>

<section class="hero">
  <div class="hero-photo" role="img" aria-label="Photo of a technician servicing a wall-mounted air conditioner while a client watches"></div>
  <h1 class="hero-title">CLIMATE SOLUTIONS ATELIER</h1>
  <p class="hero-sub">Lorem ipsum dolor sit amet, consectetur adipiscing elit, sed do eiusmod<br>tempor incididunt ut labore et dolore magna aliqua.</p>
  <a class="btn btn-fill" href="#">GET STARTED</a>
  <svg class="abs" style="left:0;top:640px" width="1200" height="110" viewBox="0 640 1200 110">
    <defs>
      <linearGradient id="bandHero" x1="0" x2="1">
        <stop offset="0" stop-color="#33b8a4"/><stop offset="1" stop-color="#3176b5"/>
      </linearGradient>
    </defs>
    <polygon points="0,664 600,746 1200,664 1200,750 0,750" fill="#ffffff"/>
    <polygon points="0,657 600,732 1200,657 1200,664 600,746 0,664" fill="url(#bandHero)"/>
  </svg>
</section>

<section class="welcome">
  <h2 class="section-title" style="top:794px">WELCOME TO ORV</h2>
  <p class="lead" style="left:190px;top:857px;width:820px">Lorem ipsum dolor sit amet, consectetur adipiscing elit, sed do eiusmod tempor incididunt ut labore et dolore magna aliqua. Ut enim ad minim veniam, quis nostrud exercitation ullamco laboris nisi ut aliquip ex ea commodo consequat. Duis aute irure dolor</p>

  <div class="card card-left">
    <h3>MAINTENANCE</h3>
    <p>Lorem ipsum dolor sit amet, consectetur adipiscing elit, sed do eiusmod tempor incididunt ut labore et dolore magna aliqua. Ut enim ad minim veniam, quis nostrud ea</p>
  </div>
  <svg class="diamond" style="left:437px" viewBox="0 0 130 130">
    <rect x="19" y="19" width="92" height="92" transform="rotate(45 65 65)" fill="#3176b5"/>
    <g fill="none" stroke="#fff" stroke-width="2.5" stroke-linecap="round" stroke-linejoin="round">
      <circle cx="72" cy="56" r="14"/><circle cx="72" cy="56" r="6"/>
      <path d="M62 66 L44 84 a4 4 0 0 0 6 6 L68 72"/>
    </g>
  </svg>

  <div class="card card-right">
    <h3>INSTALLATION</h3>
    <p>Lorem ipsum dolor sit amet, consectetur adipiscing elit, sed do eiusmod tempor incididunt ut labore et dolore magna aliqua. Ut enim ad minim veniam, quis nostrud ea</p>
  </div>
  <svg class="diamond" style="left:628px" viewBox="0 0 130 130">
    <rect x="19" y="19" width="92" height="92" transform="rotate(45 65 65)" fill="#3176b5"/>
    <g fill="none" stroke="#fff" stroke-width="2.5" stroke-linecap="round" stroke-linejoin="round">
      <rect x="46" y="48" width="34" height="16" rx="3"/>
      <path d="M38 56 H46 M80 56 H86"/>
      <path d="M56 64 V82 H70 V64"/>
      <path d="M54 88 H72"/>
    </g>
  </svg>
</section>

<section class="who">
  <div class="who-photo" role="img" aria-label="Photo of a technician in a hard hat repairing an outdoor air conditioning unit"></div>
  <div class="who-panel">
    <h2>WHO WE ARE</h2>
    <p>Lorem ipsum dolor sit amet, consectetur adipiscing elit, sed do eiusmod tempor incididunt ut labore et dolore magna aliqua. Ut enim ad minim veniam, quis nostrud exercitation ullamco laboris nisi ut aliquip ex ea commodo consequat. Duis aute irure dolor in reprehenderit in voluptate velit esse cillum dolore eu fugiat nulla pariatur.</p>
    <a class="btn btn-line" href="#">READ MORE</a>
  </div>
</section>

<section class="services">
  <h2 class="section-title" style="top:1792px">OUR SERVICES</h2>
  <p class="lead" style="left:160px;top:1846px;width:880px;font-size:19.5px">Lorem ipsum dolor sit amet, consectetur adipiscing elit, sed do eiusmod tempor incididunt ut labore et dolore magna aliqua. Ut enim ad</p>

  <div class="service" style="left:89px">
    <div class="circle" role="img" aria-label="Photo of a technician inspecting an air conditioning unit" style="background:linear-gradient(135deg,#e9ecef,#b9a89a 50%,#3b4a66)"></div>
    <h3>AIR CONDITIONING</h3>
  </div>
  <div class="service" style="left:443px">
    <div class="circle" role="img" aria-label="Photo of heating system pressure gauges" style="background:linear-gradient(135deg,#5a5f6a,#2f3340)">
      <div class="circle-overlay">Lorem ipsum dolor sit amet, consectetur adipiscing elit, sed do eiusmod tempor incididunt ut labore et dolore magna.</div>
    </div>
    <h3>HEATING</h3>
  </div>
  <div class="service" style="left:799px">
    <div class="circle" role="img" aria-label="Photo of an air treatment unit grille" style="background:linear-gradient(180deg,#7d8574 0%,#e8eaec 35%,#a0928a 60%,#8a7d76 100%)"></div>
    <h3>AIR TREATMENT</h3>
  </div>
</section>

<section class="contact">
  <h2>CONTACT US</h2>
  <div class="field" style="left:89px;top:102px;width:330px;height:52px">Name</div>
  <div class="field" style="left:435px;top:102px;width:330px;height:52px">Email</div>
  <div class="field" style="left:781px;top:102px;width:329px;height:52px">Address</div>
  <div class="field field-area" style="left:89px;top:168px;width:1021px;height:197px">Messages</div>
  <a class="btn btn-submit" href="#">SUBMIT</a>
</section>

<div class="map" role="img" aria-label="Street map showing the company location"></div>

<footer>
  <svg class="abs" style="left:0;top:3195px" width="1200" height="504" viewBox="0 3195 1200 504">
    <defs>
      <linearGradient id="bandFoot" x1="0" x2="1">
        <stop offset="0" stop-color="#33b8a4"/><stop offset="1" stop-color="#3176b5"/>
      </linearGradient>
    </defs>
    <polygon points="0,3278 600,3204 1200,3278 1200,3288 600,3214 0,3288" fill="url(#bandFoot)"/>
    <polygon points="0,3288 600,3214 1200,3288 1200,3699 0,3699" fill="#2b2b2b"/>
  </svg>

  <div class="footer-brand">ORV</div>
  <p class="footer-text footer-about">Lorem ipsum dolor sit amet, consectetur adipiscing elit, sed do eiusmod tempor incididunt ut labore et dolore magna aliqua.</p>

  <div class="footer-text footer-col" style="left:409px;top:3354px">
    <h3>QUICKS LINKS</h3>
    <ul><li>Home</li><li>Who Are We</li><li>Our Services</li><li>Presentation</li><li>Achievements</li><li>Contact</li></ul>
  </div>
  <div class="footer-text footer-col" style="left:624px;top:3354px">
    <h3>SERVICES</h3>
    <ul><li>Air Conditioning</li><li>Heating</li><li>Air Treatment</li></ul>
  </div>
  <div class="footer-text footer-col" style="left:828px;top:3354px">
    <h3>CONTACT US</h3>
    <ul><li>14 Allée des Tilleuls 38100</li><li>VAL-DES-PINS</li><li>Tel: 04 00 12 34 56</li><li>Fax: 04 00 65 43 21</li><li>contact@orv-atelier.fr</li></ul>
  </div>

  <p class="footer-text copyright">Copyright 2020 ORV &nbsp;| All Rights Reserved</p>
</footer>

</body>
</html>
```